Velqora new official website

We need a new design for our website www.velqora-example.com We are web marketing publishers and our website must be attractive for clients. That's why we need to "refresh" it. The main colour of our logo is orange, and this is an indication for the colours of the website too. We need the design for the homepage and the design of inner pages. Here is the list of the various sections of the website:
- ABOUT US: Who we are/Certificates/Offices/Team
- SERVICES: SEM/Display/Email Marketing and coregistration/ad networking
- PROJECTS/NETWORK/BRANDS: We need one page per country with screenshots of the websites and very short descriptions.
- VELQORA & CHARITY
- WORK WITH US
- CONTACT US
- NEWS

```html
<!DOCTYPE html>
<html lang="en">
<head>
<meta charset="utf-8">
<title>Velqora – Home</title>
<link href="https://fonts.googleapis.com/css2?family=Arimo:ital,wght@0,400;0,700;1,400&family=Fira+Sans:wght@400;600;700&display=swap" rel="stylesheet">
<style>
:root{
  --orange:#f7941d;
  --orange-deep:#e8730c;
  --orange-light:#fbb040;
  --brown:#5a3a12;
  --grey-bg:#e4e4e4;
  --grey-text:#555;
  --dark:#2d2d2d;
  --white:#fff;
}
*{margin:0;padding:0;box-sizing:border-box}
html,body{width:768px;height:1200px;overflow:hidden}
body{position:relative;font-family:"Arimo",Arial,sans-serif;font-size:8px;color:var(--grey-text);background:var(--grey-bg)}
.abs{position:absolute}
/* header */
.header{left:0;top:0;width:768px;height:92px;background:linear-gradient(#fafafa,#dedede)}
.topbar{right:92px;top:8px;display:flex;align-items:center;gap:6px;font-size:7.5px;color:#444}
.rss{width:9px;height:9px;background:var(--orange);border-radius:2px}
.search{width:92px;height:13px;border:1px solid #bbb;border-radius:7px;background:#fff;font-size:7px;padding-left:6px;line-height:11px;color:#888}
.go{width:16px;height:13px;border-radius:7px;background:var(--orange);color:#fff;font-size:6.5px;text-align:center;line-height:13px}
.logo{left:64px;top:38px;display:flex;align-items:center;gap:5px;font-family:"Fira Sans",sans-serif;font-weight:700;font-size:22px;color:var(--orange-deep)}
.logo .dot{width:14px;height:14px;border-radius:50%;background:var(--orange-deep)}
.nav{left:255px;top:67px;display:flex;gap:2px}
.nav a{display:block;height:24px;line-height:24px;padding:0 9px;font-size:9px;color:#fff;text-decoration:none;background:linear-gradient(#777,#444);border-radius:4px 4px 0 0}
.nav a.active{background:linear-gradient(var(--orange-light),var(--orange-deep))}
/* hero */
.hero{left:0;top:92px;width:768px;height:246px;background:linear-gradient(var(--orange-light),var(--orange) 60%,var(--orange-deep))}
.hero-title{left:78px;top:108px;font-family:"Fira Sans",sans-serif;font-weight:700;color:var(--brown);line-height:1}
.hero-title .l1{font-size:21px;color:#fff}
.hero-title .l2{font-size:30px}
.hero-title .l3{font-size:19px;color:#fff;padding-left:50px}
.hero-title .l4{font-size:22px}
.hero-text{left:92px;top:212px;width:155px;font-size:7.5px;line-height:11px;color:#fff}
.btn{display:inline-block;height:13px;line-height:13px;padding:0 10px;border-radius:7px;background:#3b3b3b;color:#fff;font-size:7.5px}
.slider{left:288px;top:104px;width:400px;height:238px;background:#fff;padding:6px;box-shadow:0 2px 6px rgba(0,0,0,.3)}
.slide-photo{width:100%;height:100%;background:linear-gradient(#f0f0f0,#cfcfcf 60%,#8a8f97)}
.caption{left:6px;top:6px;width:388px;height:20px;background:rgba(0,0,0,.65);color:#fff;font-size:10px;line-height:20px;padding-left:8px}
.ribbon{width:86px;height:18px;background:var(--orange-deep);color:#fff;font-size:9px;font-weight:700;text-align:center;line-height:18px;transform:rotate(45deg);right:-22px;top:18px}
.arrow{top:200px;width:18px;height:22px}
.tabs{left:78px;top:318px;display:flex}
.tabs div{width:88px;height:18px;line-height:18px;text-align:center;font-size:8.5px;color:#444;background:#fff;border-radius:4px 4px 0 0;margin-right:2px}
.tabs div.on{background:#d8d8d8}
/* expertise */
.fields{left:0;top:338px;width:768px;height:166px;background:linear-gradient(#d2d2d2,#e8e8e8)}
.cards{left:77px;top:364px;display:flex;gap:7px}
.card{width:118px;height:117px;background:#fff;border-radius:4px;box-shadow:0 1px 3px rgba(0,0,0,.25);padding:7px;position:relative}
.card-top{display:flex;align-items:center;gap:6px;height:32px}
.card .icon{flex:none;width:28px;height:30px;border-radius:3px;background:linear-gradient(#fbb040,#c0561b)}
.card h3{font-family:"Fira Sans",sans-serif;font-weight:600;font-size:10px;color:var(--orange);line-height:11px}
.card p{font-size:7px;line-height:9.5px;text-align:center;margin-top:6px;color:#444}
.card .more{position:absolute;left:34px;bottom:9px;width:50px;height:12px;border-radius:6px;background:var(--orange);color:#fff;font-size:7px;text-align:center;line-height:12px}
/* content */
.content{left:78px;top:504px;width:612px;height:478px;background:#fff;border-radius:5px}
.col h2{font-family:"Fira Sans",sans-serif;font-weight:600;font-size:15px;color:var(--orange)}
.col p{font-size:7.5px;line-height:11px;margin-top:8px;color:#555}
.news{width:270px;background:linear-gradient(var(--orange-light),var(--orange));border-radius:6px;box-shadow:0 2px 4px rgba(0,0,0,.2);overflow:hidden}
.news-head{height:40px;background:linear-gradient(var(--orange-deep),#d4600a);border-radius:14px 14px 0 0;color:#fff;font-family:"Fira Sans",sans-serif;font-weight:600;font-size:14px;padding:13px 0 0 10px}
.news-photo{width:128px;height:76px;background:linear-gradient(#c8c8c8,#6c5a48);border:2px solid #fff;float:left;margin:6px 8px 0 8px}
.news-intro{font-size:7.5px;line-height:11px;color:#fff;padding:8px 8px 0 0}
.bullets{clear:both;list-style:none;padding:8px}
.bullets li{font-size:7.5px;color:#fff;height:17.5px;line-height:17.5px;border-bottom:1px solid rgba(255,255,255,.35);padding-left:15px;position:relative}
.bullets li::before{content:"";position:absolute;left:2px;top:6px;width:6px;height:6px;border-radius:50%;background:#fff}
.ad-item{padding:5px 10px 3px}
.ad-item h4{font-size:7.5px;color:#fff;font-weight:700;line-height:10px}
.ad-item p{font-size:7px;color:#fff;line-height:10px;margin-top:2px}
.badges{width:270px;height:98px;background:var(--orange);border-radius:6px;padding:6px}
.badge-row{height:58px;background:#fff;border-radius:4px;display:flex;align-items:center;justify-content:space-around;padding:0 6px}
.badge{width:34px;height:34px;background:#ddd}
.badges p{font-size:6.5px;color:#fff;line-height:9px;margin-top:5px}
/* footer */
.panel{left:0;top:982px;width:768px;height:158px;background:linear-gradient(var(--orange) 0,var(--orange) 20%,#fbc77a 100%)}
.fcol{top:994px}
.fcol h3{font-family:"Fira Sans",sans-serif;font-weight:400;font-size:12.5px;color:#333;padding-left:16px;position:relative}
.fcol h3::before{content:"";position:absolute;left:0;top:2px;width:10px;height:10px;border-radius:50%;background:#333}
.quote{font-style:italic;font-size:7.5px;line-height:12px;color:#fff;margin-top:20px;padding-left:6px}
.form-row{display:flex;align-items:center;margin-top:7px;font-size:7.5px;color:#444}
.form-row span{width:85px;padding-left:12px}
.form-row i{display:block;width:120px;height:18px;background:#fff;border:1px solid #ccc;border-radius:3px}
.submit{margin:7px 0 0 143px;width:45px;height:14px;background:#333;color:#fff;font-size:7.5px;text-align:center;line-height:14px;border-radius:7px}
.addr{font-size:7px;line-height:11px;color:#444;margin-top:18px}
.bottom{left:0;top:1140px;width:768px;height:60px;background:var(--dark)}
.links{left:88px;top:1146px;color:#fff;font-size:7px}
.copy{left:88px;top:1168px;color:#ddd;font-size:6.5px;line-height:8.5px}
.flogo{right:80px;top:1155px;font-family:"Fira Sans",sans-serif;font-weight:700;font-size:19px;color:#777;display:flex;gap:5px;align-items:center}
.flogo .dot{width:12px;height:12px;border-radius:50%;background:#777}
</style>
</head>
<body>
<header class="abs header"></header>
<div class="abs topbar"><span class="rss"></span><span>Please subscribe to: Posts | Comments | Email</span><span class="search">Search...</span><span class="go">GO</span></div>
<div class="abs logo">Velqora<span class="dot"></span></div>
<nav class="abs nav">
  <a class="active">About Us</a><a>Services</a><a>Projects/Network/Brands</a><a>Velqora</a><a>Work With Us</a><a>Contact Us</a><a>News</a>
</nav>

<section class="abs hero"></section>
<div class="abs hero-title"><div class="l1">The</div><div class="l2">Main Way</div><div class="l3">of Your</div><div class="l4">Bussiness</div></div>
<p class="abs hero-text">Our aim is creating adding value on our customers sales through technology and web marketing by means of the most modern web advertising systems.</p>
<span class="abs btn" style="left:131px;top:279px">Read more</span>
<div class="abs slider">
  <div class="slide-photo" role="img" aria-label="Photo of a smiling business team in suits"></div>
  <div class="abs caption">Lorem ipsum dolor sit amet....</div>
  <div class="abs ribbon">Our Sites</div>
</div>
<svg class="abs arrow" style="left:279px" viewBox="0 0 18 22"><rect width="18" height="22" fill="#e8730c"/><path d="M12 5 5 11 12 17Z" fill="#fff"/></svg>
<svg class="abs arrow" style="left:670px" viewBox="0 0 18 22"><rect width="18" height="22" fill="#e8730c"/><path d="M6 5 13 11 6 17Z" fill="#fff"/></svg>
<div class="abs tabs"><div class="on">Fields of Expertise</div><div>Our Site</div></div>

<section class="abs fields"></section>
<div class="abs cards">
  <div class="card"><div class="card-top"><div class="icon" role="img" aria-label="Travel brochures icon"></div><h3>Tourism</h3></div><p>Tourism has been our first passion. Today it is our MAIN business and generates our MAIN income.</p><span class="more">Learn more</span></div>
  <div class="card"><div class="card-top"><div class="icon" role="img" aria-label="Smartphone icon"></div><h3>Technology &amp; Communication</h3></div><p>Dsl, lap tops, hardware, isn't that a hard job to keep updated about it?</p><span class="more">Learn more</span></div>
  <div class="card"><div class="card-top"><div class="icon" role="img" aria-label="Rising chart icon"></div><h3>Finance</h3></div><p>Velqora has been working for a long time with the MAIN brands in the international world of finance.</p><span class="more">Learn more</span></div>
  <div class="card"><div class="card-top"><div class="icon" role="img" aria-label="Perfume bottle icon"></div><h3>Fashion</h3></div><p>The new frontier for our company is the world of fashion. We believe that today, television...</p><span class="more">Learn more</span></div>
  <div class="card"><div class="card-top"><div class="icon" role="img" aria-label="Household appliance icon"></div><h3>Durable Goods</h3></div><p>As publisher we help the MAIN brands in the field of automotive, appliances, business equipment...</p><span class="more">Learn more</span></div>
</div>

<main class="abs content">
  <div class="abs col" style="left:14px;top:10px;width:270px">
    <h2>Scope and Mission</h2>
    <p>Our aim is creating adding value on our customers sales through technology and web marketing by means of the most modern web advertising systems. We help our customers in developing new sales strategies based on the web marketing. We watch the market and support our customers in achieving excellent visibility on the newest advertising channels. We are able to offer a wide range of either standard or tailored solutions.</p>
  </div>
  <span class="abs btn" style="left:228px;top:112px">Read more</span>
  <div class="abs col" style="left:334px;top:10px;width:270px">
    <h2>Clients' strategies and web know how</h2>
    <p>Our aim is creating adding value on our customers sales through technology and web marketing by means of the most modern web advertising systems. We help our customers in developing new sales strategies based on the web marketing. We watch the market and support our customers in achieving excellent visibility on the newest advertising channels.</p>
  </div>
  <span class="abs btn" style="left:545px;top:112px">Read more</span>

  <div class="abs news" style="left:10px;top:146px;height:282px">
    <div class="news-head">Velqora News</div>
    <div class="news-photo" role="img" aria-label="Photo of a crowded trade fair hall"></div>
    <p class="news-intro">We cooperate with the MAIN international brands in the fields of tourism, finance, fashion, durable goods, technologies...</p>
    <span class="btn" style="margin:4px 0 0 36px">Read more</span>
    <ul class="bullets">
      <li>Simply dummy text of the printing and typesetting industry.</li>
      <li>Lorem has been the industry's standard dummy text.</li>
      <li>Ever since then, when an unknown printer.</li>
      <li>Has been the industry's standard dummy text ever since then.</li>
      <li>Simply dummy text of the printing and typesetting industry.</li>
      <li>Lorem Ipsum has been the industry's standard dummy text.</li>
      <li>Ever since then when an unknown printer.</li>
    </ul>
  </div>

  <div class="abs news" style="left:332px;top:146px;height:180px">
    <div class="news-head">Adtech News</div>
    <div class="ad-item"><h4>The Fate of On-Page SEO Content: Relevance, Not Rankings</h4><p>From an SEO perspective, on-page content is about helping establish what search queries your page might be relevant to...</p></div>
    <div class="ad-item"><h4>Harrow Labs Is About To Change Marketplace... Again.</h4><p>Harrow Labs begins beta testing of a new inventory and delivery tool for marketplace...</p></div>
    <div class="ad-item"><h4>Idea Boards: What You Need To Know When Updating AdBoard Bid Types</h4><p>Max CPC, Enhanced CPC, Automatic Bidding – each option carries a distinct set of pros...</p></div>
  </div>

  <div class="abs badges" style="left:332px;top:334px">
    <div class="badge-row">
      <span class="badge" style="background:#f7941d;border-radius:50%"></span>
      <span class="badge" style="background:#cfd8e0"></span>
      <span class="badge" style="background:#d9d9d9"></span>
      <span class="badge" style="background:#e24d2b"></span>
      <span class="badge" style="background:#c8102e;border-radius:50%"></span>
    </div>
    <p>VELQORA, Via Nardelli 14 - 40100 Lorvano (LV) Italy, Tel +39 000 555 0148 - Fax +39 000 555 0149, VAT IT 00000000000</p>
  </div>
</main>

<footer class="abs panel"></footer>
<div class="abs fcol" style="left:92px;width:160px">
  <h3>Testimonials</h3>
  <p class="quote">"Lorem Ipsum is simply dummy text of the printing and typesetting industry. Lorem Ipsum has been the industry's standard text ever since the 1500s, when an unknown printer dummy..."</p>
</div>
<div class="abs fcol" style="left:272px;width:210px">
  <h3>Newsletter</h3>
  <p class="addr" style="margin-top:12px">Duis aute irure dolor in reprehenderit in voluptate velit esse cillum dolore eu fugiat nulla pariatur.</p>
  <div class="form-row"><span>Your Name</span><i></i></div>
  <div class="form-row"><span>Your Email Address</span><i></i></div>
  <div class="submit">Submit</div>
</div>
<div class="abs fcol" style="left:502px;width:180px">
  <h3>Contact us</h3>
  <p class="addr">HEAD OFFICE: Velqora srl - Via Nardelli 14<br>40100 Lorvano (LV) - ITALY<br>Tel +39 000 555 0148 Fax +39 000 555 0149<br>BRANCH OFFICE: 8/17 Garden Terrace<br>Port Kesari - INDIA<br>BRANCH OFFICE: Meridian House, Lotus Road<br>Navapur 110 - INDIA<br>BRANCH OFFICE: Calle Ostera 21, Velmar</p>
</div>

<div class="abs bottom"></div>
<div class="abs links">About Site &nbsp;|&nbsp; Security &nbsp;|&nbsp; Privacy Policy &nbsp;|&nbsp; Contact Us &nbsp;|&nbsp; Help</div>
<p class="abs copy">Copyright © 2011 www.velqora-example.com. All Rights Reserved.<br>Designated trademarks and brands are the property of their respective owners.<br>Use of this Web site constitutes acceptance of the www.velqora-example.com User Agreement and Privacy Policy.</p>
<div class="abs flogo">Velqora<span class="dot"></span></div>
</body>
</html>
```